Business Card Design Project - Sports Brand

Brisk is a e-commerce fitness wear brand for ladies who are into gym, pole and swim.

Card should not be overly cluttered and should include the following:

1. logo
2. Name of the company (Use "Brisk Loom Pte Ltd" for now)
3. Address of company (Use a mock address)
4. Representative's name and contact info etc. (use a mock name and contact info)
5. website address

Target Market(s)

Women who are into pole , gym, and swim.

Women who shop online

Industry/Entity Type

E-Commerce

Colors

Designer to choose colors to be used in the design.

Requirements
Nice to have
• feminine sublimation of colours

Need not be printed on traditional paper. We would like the design to be revolutionary and interesting to the eye :)
Should not have
• the design should not be traditional looking. Do not include illustrations of Bikinis, yoga poses etc. in the card.

```html
<!DOCTYPE html>
<html lang="en">
<head>
<meta charset="utf-8">
<title>Brisk Loom Pte Ltd — Business Card</title>
<link rel="stylesheet" href="https://fonts.googleapis.com/css2?family=Cinzel:wght@400&family=Lato:wght@400;700;900&family=Raleway:wght@200&display=swap">
<style>
  :root {
    --backdrop: #2a2a2c;
    --card-white: #fbfbfb;
    --card-shade: #ececec;
    --pink-deep: #e64a78;
    --pink-soft: #f39bbd;
    --brand-red: #c0213f;
    --brand-coral: #ec5c6c;
    --ink: #1f1f1f;
    --icon-pink: #d94a78;
    --white: #ffffff;
  }
  * { margin: 0; padding: 0; box-sizing: border-box; }
  html, body { width: 1200px; height: 900px; overflow: hidden; }
  body {
    background: var(--backdrop);
    font-family: "Lato", sans-serif;
    position: relative;
  }
  .card {
    position: absolute;
    left: 267px;
    width: 666px;
    height: 380px;
    border-radius: 26px;
    overflow: hidden;
    background: linear-gradient(160deg, var(--card-white) 0%, var(--card-shade) 100%);
    box-shadow: 0 14px 30px rgba(0,0,0,.45);
  }
  .card--back { top: 50px; }
  .card--front { top: 470px; }

  /* back side */
  .back-logo {
    position: absolute;
    top: 0; left: 0; right: 0;
    height: 270px;
    display: flex; align-items: center; justify-content: center; gap: 22px;
  }
  .brand-dot {
    width: 96px; height: 96px; border-radius: 50%;
    background: radial-gradient(circle at 40% 45%, var(--brand-coral), var(--pink-deep));
  }
  .brand-name {
    font-family: "Lato", sans-serif;
    font-weight: 900;
    color: var(--brand-red);
    font-size: 84px;
    letter-spacing: 1px;
  }
  .back-band {
    position: absolute;
    left: 0; right: 0; bottom: 0;
    height: 110px;
    background: linear-gradient(90deg, var(--pink-soft), var(--pink-deep));
    display: flex; align-items: center; justify-content: center;
  }
  .company-name {
    font-family: "Raleway", sans-serif;
    font-weight: 200;
    font-size: 50px;
    color: var(--white);
    letter-spacing: 1px;
  }

  /* front side */
  .front-band {
    position: absolute;
    top: 0; left: 0; right: 0;
    height: 84px;
    background: linear-gradient(90deg, var(--pink-deep), var(--pink-soft));
    text-align: right;
    padding: 14px 30px 0 0;
    color: var(--white);
  }
  .person-name {
    font-family: "Cinzel", serif;
    font-size: 30px;
    line-height: 1;
    letter-spacing: 1px;
  }
  .person-role {
    font-weight: 700;
    font-size: 17px;
    margin-top: 3px;
  }
  .front-logo {
    position: absolute;
    top: 104px; left: 0; right: 0;
    display: flex; align-items: center; justify-content: center; gap: 16px;
  }
  .front-logo .brand-dot { width: 64px; height: 64px; }
  .front-logo .brand-name { font-size: 58px; }
  .contact-grid {
    position: absolute;
    top: 212px; left: 126px;
    display: grid;
    grid-template-columns: auto auto;
    column-gap: 34px; row-gap: 10px;
  }
  .contact-item {
    display: flex; align-items: center; gap: 10px;
    font-weight: 700; font-size: 19px; color: var(--ink);
    white-space: nowrap;
  }
  .contact-item svg { width: 20px; height: 20px; flex: none; fill: var(--icon-pink); }
  .contact-item .accent { color: var(--brand-red); }
  .address {
    position: absolute;
    left: 36px; right: 20px; bottom: 36px;
    font-size: 19px;
  }
</style>
</head>
<body>

<section class="card card--back" aria-label="Card back">
  <div class="back-logo">
    <span class="brand-dot" aria-hidden="true"></span>
    <span class="brand-name">Brisk</span>
  </div>
  <div class="back-band">
    <span class="company-name">Brisk Loom Pte Ltd</span>
  </div>
</section>

<section class="card card--front" aria-label="Card front">
  <header class="front-band">
    <div class="person-name">YOUR NAME</div>
    <div class="person-role">Designation</div>
  </header>

  <div class="front-logo">
    <span class="brand-dot" aria-hidden="true"></span>
    <span class="brand-name">Brisk</span>
  </div>

  <div class="contact-grid">
    <div class="contact-item">
      <svg viewBox="0 0 24 24" aria-hidden="true"><path d="M4 9c0-3 4-5 8-5s8 2 8 5l-3 1-1-2c-2-.6-6-.6-8 0l-1 2zM6 12h12l2 8H4z"/></svg>
      (852) 5550 1942
    </div>
    <div class="contact-item">
      <svg viewBox="0 0 24 24" aria-hidden="true"><path d="M10.6 13.4a4 4 0 0 0 5.7 0l3-3a4 4 0 0 0-5.7-5.7l-1.2 1.2 1.4 1.4 1.2-1.2a2 2 0 0 1 2.9 2.9l-3 3a2 2 0 0 1-2.9 0zM13.4 10.6a4 4 0 0 0-5.7 0l-3 3a4 4 0 0 0 5.7 5.7l1.2-1.2-1.4-1.4-1.2 1.2a2 2 0 0 1-2.9-2.9l3-3a2 2 0 0 1 2.9 0z"/></svg>
      <span>www.<span class="accent">briskloom-shop</span>.com</span>
    </div>
    <div class="contact-item">
      <svg viewBox="0 0 24 24" aria-hidden="true"><path d="M7 2h10a1 1 0 0 1 1 1v18a1 1 0 0 1-1 1H7a1 1 0 0 1-1-1V3a1 1 0 0 1 1-1zm1 2v14h8V4zm3 15v1h2v-1z"/></svg>
      (852) 5550 1942
    </div>
    <div class="contact-item">
      <svg viewBox="0 0 24 24" aria-hidden="true"><path d="M2 5h20v14H2zm2 2v.4l8 5.6 8-5.6V7zm0 2.8V17h16V9.8l-8 5.6z"/></svg>
      hello@briskloom-shop.com
    </div>
  </div>

  <div class="contact-item address">
    <svg viewBox="0 0 24 24" aria-hidden="true"><path d="M12 3l10 9h-3v8h-5v-5h-4v5H5v-8H2z"/></svg>
    48 Fernvale Trade Street #03-11 Harbourline Hub Singapore 500123
  </div>
</section>

</body>
</html>
```